Card Design Project

A simple, funky, cool birth announcement card
Not corporate, but arty
Not childish nor girlish
No baby pictures

Text is tbc (eg name and date may change)

Front side: just the name "roos"
Should be easy to read

Back side text (in Dutch):

We vinden je nu al leuk!

20 JUNE 2013
Singapore

Dochter van Marieke Vos & Geert Bakker

Yangon, Myanmar
+95 1 48 7361
Skype: Marieke.Vos
Skype: Geert.Bakker

Size will be A6
Updates

Reason: Dear designers, At this stage we would like to have one or more designers to draft up the card (of which the final text is still tbd as the baby is yet to be born) using the typeface used on the left below (or similar!) of the newly added picture - in black - in fluorescent colours Can you get back to us in a few days? Thanks

Target Market(s)

Our funky friends in holland.

Industry/Entity Type

Baby

Requirements
Must have
• Colours, aswe are very happy to welcome this baby.
Something that makes it stand out from all other baby birth announcement cards

A6 size
Deadline 21 June
Printing will be on white (thick paper 250g)
Design for 5mm "bleedsides" all around
At least available in PDF (and other formats)
Nice to have
• We've recently moved from netherlands to Yangon
We could include the iconic thirikyaw pagoda

I would like for it to look like a cool party announcement

Include bright fluoriscent colours, including orange.
The enveloppe will be orange
Should not have
• Any baby stuff, soft pink dominance, childish stuff.

```html
<!DOCTYPE html>
<html lang="nl">
<head>
<meta charset="utf-8">
<title>Geboortekaart Roos</title>
<link href="https://fonts.googleapis.com/css2?family=Amatic+SC:wght@400;700&display=swap" rel="stylesheet">
<style>
  :root {
    --lime: #a6f01e;
    --lime-soft: #9cec5a;
    --teal: #79e6d3;
    --white: #ffffff;
    --text-light: #f2fff0;
    --page: #ffffff;
  }
  * { margin: 0; padding: 0; box-sizing: border-box; }
  html, body {
    width: 1200px; height: 465px; overflow: hidden;
    background: var(--page);
  }
  .spread { position: relative; width: 1200px; height: 465px; }
  .card {
    position: absolute; top: 33px;
    width: 555px; height: 395px; overflow: hidden;
    box-shadow: 0 1px 4px rgba(0,0,0,0.18);
  }
  .card--front {
    left: 33px;
    background: linear-gradient(90deg, var(--lime) 0%, var(--lime) 28%, var(--lime-soft) 42%, var(--teal) 58%, var(--teal) 100%);
  }
  .card--back {
    left: 613px;
    background: linear-gradient(90deg, var(--lime-soft) 0%, #90ea8a 8%, var(--teal) 22%, var(--teal) 100%);
  }
  .ornament { position: absolute; top: 0; right: 0; height: 395px; }
  .card--front .ornament { width: 250px; }
  .card--back .ornament { width: 330px; }
  .baby-name {
    position: absolute; left: 40px; top: 18px;
    font-family: "Amatic SC", "Comic Sans MS", cursive;
    font-weight: 400; font-size: 236px; line-height: 1;
    letter-spacing: 4px; text-transform: uppercase;
    color: #eefcff;
    text-shadow: 0 0 14px rgba(60,120,110,0.45);
  }
  .details {
    position: absolute; left: 55px; top: 30px;
    font-family: "Amatic SC", "Comic Sans MS", cursive;
    font-weight: 400; font-size: 27px; line-height: 31px;
    color: var(--text-light); list-style: none;
  }
  .details .gap { height: 30px; }
</style>
</head>
<body>
<main class="spread">
  <section class="card card--front" aria-label="Voorkant">
    <h1 class="baby-name">Roos</h1>
    <svg class="ornament" viewBox="0 0 250 395" role="img" aria-label="Decoratieve witte krullen en bloemetjes op een limoengroene golf">
      <defs>
        <linearGradient id="orn-front" x1="0" y1="0" x2="1" y2="1">
          <stop offset="0" stop-color="#b8f45a"/>
          <stop offset="1" stop-color="#9be82c"/>
        </linearGradient>
      </defs>
      <path d="M250 0 L170 0 C120 80 150 170 90 240 C50 290 40 340 60 395 L250 395 Z" fill="url(#orn-front)"/>
    </svg>
  </section>

  <section class="card card--back" aria-label="Achterkant">
    <ul class="details">
      <li>We vinden je nu al leuk!</li>
      <li class="gap"></li>
      <li>Wanneer ______</li>
      <li>Waar ________</li>
      <li class="gap"></li>
      <li>Dochter van Marieke Vos &amp; Geert Bakker</li>
      <li class="gap"></li>
      <li>Yangon, Myanmar</li>
      <li>+95 1 48 7361</li>
      <li>Skype: Marieke.Vos</li>
      <li>Skype: Geert.Bakker</li>
    </ul>
    <svg class="ornament" viewBox="0 0 330 395" role="img" aria-label="Decoratieve witte krullen en bloemetjes op een limoengroene golf">
      <defs>
        <linearGradient id="orn-back" x1="0" y1="0" x2="1" y2="1">
          <stop offset="0" stop-color="#b8f45a"/>
          <stop offset="1" stop-color="#9be82c"/>
        </linearGradient>
      </defs>
      <path d="M330 0 L290 0 C250 90 280 170 220 250 C180 300 170 350 180 395 L330 395 Z" fill="url(#orn-back)"/>
    </svg>
  </section>
</main>
</body>
</html>
```